New Business Card Design Project

The look of the business cards should include
-Clean Lines
-Should suit a sophisticated customer
-Evoke a mix of business and creativity
-Incorporate the color Gray or Black:White palette
-Open to see layouts in both vertical and horizontal
3 partners (we need 3 cards)
NORELLE VASK
ODA TRENCHARD
MARU ELDFORTH
Reason: We would like more submissions please
Target Market(s)
We are a NYC and European based boutique consulting agency specializing in fashion business and creative clients. In addition to consulting we will be offering an e-commerce site selling women’s accessories and jewelry geared towards fashion forward women ages 25-50.
Industry/Entity Type
Business
Font styles to use
Requirements
Must have
- - texture
- grayscale
3 Partners
Details for each card
CONSULTING I DESIGN
MARU ELDFORTH
Founding Partner
917.555.0183
maru@theplumwickhouse.com
www.theplumwickhouse.com
CONSULTING I DESIGN
NORELLE VASK
Founding Partner
917.555.0147
norelle@theplumwickhouse.com
www.theplumwickhouse.com
CONSULTING I DESIGN
Oda Kestlin Trenchard
Founding Partner
(no phone for her)
Oda@theplumwickhouse.com
www.theplumwickhouse.com

```html
<!DOCTYPE html>
<html lang="en">
<head>
<meta charset="utf-8">
<title>The Plumwick House — Business Card</title>
<link rel="stylesheet" href="https://fonts.googleapis.com/css2?family=Source+Sans+3:wght@300;400&display=swap">
<style>
  :root {
    --backdrop: #e6e4e7;
    --card: #ffffff;
    --ink: #2b2b2b;
    --ink-soft: #3a3a3a;
    --edge: #d2d0d3;
  }
  * { margin: 0; padding: 0; box-sizing: border-box; }
  html, body {
    width: 1200px;
    height: 900px;
    overflow: hidden;
    background: var(--backdrop);
    font-family: "Source Sans 3", sans-serif;
    color: var(--ink);
  }
  .card-set {
    position: absolute;
    top: 240px;
    left: 160px;
    display: flex;
    gap: 40px;
  }
  .card {
    width: 420px;
    height: 420px;
    background: var(--card);
    border: 1px solid var(--edge);
    position: relative;
    box-shadow: 0 2px 6px rgba(0,0,0,0.08);
  }
  .card-front {
    display: flex;
    align-items: center;
    justify-content: center;
  }
  .brand-name {
    font-weight: 400;
    font-size: 30px;
    letter-spacing: 0.04em;
    color: var(--ink);
    white-space: nowrap;
  }
  .card-back {
    text-align: center;
  }
  .card-back > * {
    position: absolute;
    left: 0;
    right: 0;
  }
  .services {
    top: 38px;
    font-size: 27px;
    font-weight: 400;
    letter-spacing: 0.02em;
    color: var(--ink-soft);
  }
  .partner-name {
    top: 174px;
    font-size: 38px;
    font-weight: 300;
    letter-spacing: 0.01em;
    line-height: 1.2;
  }
  .partner-title {
    top: 226px;
    font-size: 17px;
    font-weight: 400;
    color: var(--ink-soft);
  }
  .contact {
    top: 290px;
    list-style: none;
    font-size: 20px;
    line-height: 32px;
    font-weight: 400;
  }
</style>
</head>
<body>
  <main class="card-set">
    <section class="card card-front" aria-label="Card front">
      <p class="brand-name">The Plumwick House</p>
    </section>
    <section class="card card-back" aria-label="Card back">
      <p class="services">CONSULTING I DESIGN</p>
      <h1 class="partner-name">MARU ELDFORTH</h1>
      <p class="partner-title">Founding Partner</p>
      <ul class="contact">
        <li>917.555.0183</li>
        <li>maru@theplumwickhouse.com</li>
        <li>www.theplumwickhouse.com</li>
      </ul>
    </section>
  </main>
</body>
</html>
```